Book Cover for Productivity Book

I need a book cover for my latest publication "On Momentum: The Gathered Insights of the Busiest Woman Living"

You can see my branding at www.brightmarrow.example

This is meant to be my epic pinaccle work on productivity, I want it to look like the end all be all word on productivity.

Target Market(s)

entrepreneurs

```html
<!DOCTYPE html>
<html lang="en">
<head>
<meta charset="utf-8">
<title>On Momentum — Book Cover</title>
<link rel="stylesheet" href="https://fonts.googleapis.com/css2?family=Mulish:wght@300;400;600;700;800&display=swap">
<style>
  :root {
    --page-bg: #ffffff;
    --cover-bg: #efefef;
    --cover-edge: #d9d9d9;
    --frame-line: #cfcfcf;
    --brand-red: #d0141a;
    --ink: #141414;
  }
  * { box-sizing: border-box; margin: 0; padding: 0; }
  html, body {
    width: 1200px;
    height: 1200px;
    overflow: hidden;
    background: var(--page-bg);
  }
  .canvas {
    position: relative;
    width: 1200px;
    height: 1200px;
    font-family: "Mulish", "Helvetica Neue", Arial, sans-serif;
  }
  .cover {
    position: absolute;
    left: 250px;
    top: 60px;
    width: 700px;
    height: 1080px;
    background: var(--cover-bg);
    border: 1px solid var(--cover-edge);
    text-align: center;
  }
  .cover-frame {
    position: absolute;
    inset: 16px;
    border: 1px solid var(--frame-line);
  }
  .series-word {
    position: absolute;
    top: 182px;
    left: 0;
    right: 0;
    font-weight: 700;
    font-size: 30px;
    line-height: 1;
    letter-spacing: 0.12em;
    color: var(--ink);
    text-transform: uppercase;
  }
  .title {
    position: absolute;
    top: 268px;
    left: 0;
    right: 0;
    font-weight: 700;
    font-size: 62px;
    line-height: 1;
    letter-spacing: 0.07em;
    color: var(--brand-red);
  }
  .title-reflection {
    position: absolute;
    top: 332px;
    left: 0;
    right: 0;
    font-weight: 700;
    font-size: 62px;
    line-height: 1;
    letter-spacing: 0.07em;
    color: var(--brand-red);
    transform: scaleY(-1);
    opacity: 0.16;
    -webkit-mask-image: linear-gradient(to top, #000 0%, transparent 70%);
    mask-image: linear-gradient(to top, #000 0%, transparent 70%);
  }
  .subtitle {
    position: absolute;
    top: 440px;
    left: 0;
    right: 0;
    color: var(--ink);
    font-weight: 600;
    letter-spacing: 0.16em;
    text-transform: uppercase;
  }
  .subtitle .line { display: block; }
  .subtitle .line-sm { font-size: 27px; line-height: 52px; }
  .subtitle .line-lg { font-size: 32px; line-height: 62px; }
  .subtitle .small { font-size: 21px; }
  .brand-mark {
    position: absolute;
    top: 908px;
    left: 0;
    right: 0;
    font-weight: 700;
    font-size: 22px;
    letter-spacing: 0.08em;
    color: var(--brand-red);
    text-transform: uppercase;
    white-space: nowrap;
  }
  .author {
    position: absolute;
    top: 982px;
    left: 0;
    right: 0;
    font-size: 32px;
    letter-spacing: 0.08em;
    color: var(--ink);
    text-transform: uppercase;
  }
  .author .given { font-weight: 300; }
  .author .family { font-weight: 700; }
</style>
</head>
<body>
  <main class="canvas">
    <section class="cover" aria-label="Front cover of On Momentum">
      <div class="cover-frame"></div>
      <div class="series-word">On</div>
      <h1 class="title">MOMENTUM</h1>
      <div class="title-reflection" aria-hidden="true">MOMENTUM</div>
      <p class="subtitle">
        <span class="line line-sm"><span class="small">The</span> Gathered</span>
        <span class="line line-lg">Insights</span>
        <span class="line line-sm small">Of</span>
        <span class="line line-sm">The Busiest Woman</span>
        <span class="line line-sm">Living</span>
      </p>
      <div class="brand-mark">Bright Marrow</div>
      <p class="author"><span class="given">Noa</span> <span class="family">Kessler</span></p>
    </section>
  </main>
</body>
</html>
```